Dentistry

Dentist's personal business card. No logo needed. The card shoul deliver the massage of reliability, professionalism, experience.
Please ad the full brief of the project: down the line it says: the winning look should be precise and pristine NO pictures of Teeth, smiles, instruments etc.

The details to be desplaid are:
Dr. Rob Valdoni
Doctor of Dental Surgery
PHD
Web. Www.drvaldoni.com
Email. Rob@drvaldoni.com
Tel 07731482590
Surgery address. 27Bharwick road London SW4 7QN UK
82 Fenwyn Row London SW3 2HT. Uk

Reason: Decided to make the payment unrefundable in order to get more designers involved.

Requirements
Should not have
• Logo, teeth, smile any sort of instruments.

```html
<!DOCTYPE html>
<html lang="en">
<head>
<meta charset="utf-8">
<title>Dr. Rob Valdoni – Business Card</title>
<link rel="stylesheet" href="https://fonts.googleapis.com/css2?family=Jost:wght@400&family=Source+Sans+3:wght@400&display=swap">
<style>
  :root {
    --charcoal: #3a3a3a;
    --ink: #2b2b2b;
    --paper: #ffffff;
    --backdrop: #e4e0da;
    --rule: #2f2f2f;
  }
  * { margin: 0; padding: 0; box-sizing: border-box; }
  html, body {
    width: 1115px;
    height: 1200px;
    overflow: hidden;
    background: var(--backdrop);
  }
  .canvas {
    position: relative;
    width: 1115px;
    height: 1200px;
  }
  .card {
    position: absolute;
    left: 173px;
    width: 768px;
    height: 427px;
    background: var(--paper);
    box-shadow: 0 3px 10px rgba(0,0,0,0.18);
  }
  .card--front { top: 88px; }
  .card--back { top: 687px; }

  .name-band {
    position: absolute;
    left: 8px; top: 8px;
    width: 752px; height: 164px;
    background: var(--charcoal);
    color: var(--paper);
    text-align: center;
  }
  .name-band__name {
    font-family: "Jost", sans-serif;
    font-weight: 400;
    font-size: 60px;
    line-height: 1;
    padding-top: 34px;
    letter-spacing: 0.5px;
  }
  .name-band__title {
    font-family: "Jost", sans-serif;
    font-weight: 400;
    font-size: 22px;
    margin-top: 10px;
  }

  .rule {
    position: absolute;
    left: 8px;
    width: 752px;
    height: 3px;
    background: var(--rule);
  }
  .rule--top { top: 196px; }
  .rule--bottom { top: 247px; }

  .details {
    position: absolute;
    top: 207px;
    font-family: "Source Sans 3", sans-serif;
    font-weight: 400;
    color: var(--ink);
  }
  .details__heading {
    font-weight: 400;
    font-size: 24px;
    line-height: 32px;
    margin-bottom: 33px;
  }
  .details__lines {
    font-size: 22px;
    line-height: 29px;
  }
  .details--surgery { left: 48px; text-align: left; }
  .details--contact { left: 234px; width: 300px; text-align: center; }
  .details--contact .details__lines { font-size: 25px; line-height: 32px; margin-top: -5px; }
  .details--home { right: 51px; text-align: right; }

  .back-panel {
    position: absolute;
    left: 8px; top: 8px;
    width: 752px; height: 411px;
    background: var(--charcoal);
    display: flex;
    align-items: center;
    justify-content: center;
  }
  .back-panel__name {
    font-family: "Jost", sans-serif;
    font-weight: 400;
    font-size: 56px;
    color: var(--paper);
    letter-spacing: 0.5px;
  }
</style>
</head>
<body>
<main class="canvas">

  <section class="card card--front" aria-label="Business card front">
    <header class="name-band">
      <h1 class="name-band__name">Dr. Rob Valdoni</h1>
      <p class="name-band__title">Doctor of Dental Surgery, PhD</p>
    </header>
    <div class="rule rule--top"></div>
    <div class="rule rule--bottom"></div>

    <div class="details details--surgery">
      <h2 class="details__heading">Surgery address</h2>
      <p class="details__lines">82 Fenwyn Row<br>London<br>SW3 2HT<br>UK</p>
    </div>
    <div class="details details--contact">
      <h2 class="details__heading">Contact Info</h2>
      <p class="details__lines">07731 482 590<br>rob@drvaldoni.com<br>www.drvaldoni.com</p>
    </div>
    <div class="details details--home">
      <h2 class="details__heading">Home address</h2>
      <p class="details__lines">27 Bharwick road<br>London<br>SW4 7QN<br>UK</p>
    </div>
  </section>

  <section class="card card--back" aria-label="Business card back">
    <div class="back-panel">
      <p class="back-panel__name">Rob Valdoni</p>
    </div>
  </section>

</main>
</body>
</html>
```